Tom Pelling Personal Website Yoga Teacher and Personal Fitness Trainer

Let's pick a WORDPRESS theme that can work with Video Bckground. I would like a website design to look like some of nice Squarespace themes.
I would like to have a Video background of me teaching. I can provide video. Please view my current Wordpress site: www.tompelling.example. I also have new logo. See file tpel1.png

Reason: I am guaranteeing this project because i believe designers can deliver. I am extending 5 days because the homepage image/video slider is intricate and takes a bit of time. I have provided details, images, video etc. in Dropbox. Tx

Target Market(s)

All people needing & wanting personal help (they can trust and feel safe and nurtured) for their health (wellness, nutrition, fitness, exercise). And people wanting extraordinary yoga teaching.

Industry/Entity Type

Fitness

Number of Pages Required

5+ page

Colors
9bcb3b
add136
cadf82
eaf2ce

Requirements
Must have
• Template that can use a video background
Nice to have
• Need to show good image gallery and testimonial videos

```html
<!DOCTYPE html>
<html lang="en">
<head>
<meta charset="utf-8">
<title>Tom Pelling — Yoga &amp; Wellness</title>
<link rel="stylesheet" href="https://fonts.googleapis.com/css2?family=Open+Sans:wght@300;400;600;700&family=Great+Vibes&display=swap">
<style>
  :root{
    --green:#9bcb3b;
    --green-deep:#add136;
    --green-soft:#cadf82;
    --green-pale:#eaf2ce;
    --band:#a8d165;
    --ink:#1c1c1c;
    --text:#666;
    --rule:#e3e3e3;
    --white:#fff;
  }
  *{margin:0;padding:0;box-sizing:border-box}
  html,body{width:1200px;height:2663px;overflow:hidden}
  body{position:relative;background:var(--white);font-family:"Open Sans",Arial,sans-serif;color:var(--ink)}
  .abs{position:absolute}

  /* hero */
  .hero{left:0;top:0;width:1200px;height:744px;
    background:
      radial-gradient(ellipse 120px 110px at 470px 60px,rgba(214,92,96,.75),rgba(214,92,96,0) 100%),
      radial-gradient(ellipse 110px 140px at 30px 200px,rgba(214,150,60,.7),rgba(214,150,60,0) 100%),
      radial-gradient(ellipse 110px 150px at 1120px 200px,rgba(70,120,100,.75),rgba(70,120,100,0) 100%),
      radial-gradient(ellipse 520px 260px at 640px 330px,rgba(214,160,130,.55),rgba(214,160,130,0) 100%),
      radial-gradient(ellipse 300px 140px at 600px 230px,rgba(225,130,80,.35),rgba(225,130,80,0) 100%),
      linear-gradient(180deg,#7e6a66 0%,#8c6f64 35%,#8a6253 65%,#6a4332 85%,#57392a 100%)}
  .brand{left:98px;top:26px;color:var(--white);display:flex;align-items:center;gap:12px}
  .brand-dot{width:40px;height:40px;border-radius:50%;border:2px solid var(--white)}
  .brand-name{font-size:22px;font-weight:600;letter-spacing:1px;line-height:1}
  .brand-tag{font-size:10px;font-weight:400;margin-top:5px;letter-spacing:.3px}
  .nav{left:421px;top:33px;display:flex;gap:25px;font-size:13px;color:var(--white);white-space:nowrap}
  .search{left:1078px;top:33px}
  .arrow{top:399px;width:36px;height:36px}
  .arrow.prev{left:30px}.arrow.next{left:1127px}
  .hero-panel{left:188px;top:485px;width:824px;height:259px;background:rgba(155,203,59,.82);text-align:center;color:var(--white)}
  .hero-title{margin-top:42px;font-size:42px;font-weight:400;line-height:58px}
  .hero-text{margin:10px auto 0;width:700px;font-size:15.5px;line-height:25px}
  .btn-outline{display:inline-block;margin-top:16px;width:165px;height:41px;line-height:39px;border:1px solid var(--white);font-size:17px}

  /* sections */
  .section-title{left:0;width:1200px;text-align:center;font-size:36px;font-weight:300;letter-spacing:.5px}
  .section-title b{font-weight:700}
  .section-text{left:220px;width:760px;text-align:center;font-size:15px;line-height:28px;color:var(--text)}
  .read-more{left:0;width:1200px;text-align:center;color:var(--green);font-size:15px}
  .rule{left:98px;width:1004px;height:1px;background:var(--rule)}

  .tile{display:block}
  .overlay{background:rgba(155,203,59,.85);color:var(--white);text-align:center}
  .overlay-label{position:absolute;left:0;width:100%;top:255px;font-size:17px;font-weight:600}
  .overlay svg{position:absolute;left:140px;top:192px}
  .play{position:absolute;left:50%;top:50%;transform:translate(-50%,-50%)}

  /* subscribe */
  .subscribe{left:0;top:2409px;width:1200px;height:193px;background:var(--band)}
  .sub-brand{left:110px;top:2470px;font-size:20px;font-weight:600;color:var(--white);width:140px;text-align:center}
  .sub-title{left:280px;top:2444px;font-size:38px;font-weight:400;color:var(--white);line-height:1}
  .sub-script{left:275px;top:2492px;font-family:"Great Vibes",cursive;font-size:50px;color:var(--white);line-height:1}
  .field{left:513px;top:2455px;width:531px;height:41px;border:2px solid var(--white);color:var(--white);font-size:13px;padding:0 14px;line-height:37px}
  .sub-btn{left:513px;top:2512px;width:531px;height:44px;background:var(--white);color:var(--green);text-align:center;font-size:13px;line-height:44px}

  .copyright{left:100px;top:2622px;font-size:14px;color:var(--ink)}
  .social{left:943px;top:2620px;display:flex;gap:12px}
  .social span{width:21px;height:21px;border-radius:50%}
</style>
</head>
<body>

<section class="abs hero" role="img" aria-label="Group photo of smiling yoga teacher trainees standing before a painted lotus wall"></section>

<header>
  <div class="abs brand">
    <span class="brand-dot"></span>
    <div><div class="brand-name">TOM PELLING</div><div class="brand-tag">Yoga and Wellness for Life</div></div>
  </div>
  <nav class="abs nav">
    <span>Home</span><span>About</span><span>Blog</span><span>Clients</span><span>Contact</span><span>Media</span><span>Nutrion</span><span>Schedule/Classes</span><span>Services</span>
  </nav>
  <svg class="abs search" width="22" height="22" viewBox="0 0 22 22"><circle cx="8" cy="8" r="6" fill="none" stroke="#fff" stroke-width="2.5"/><line x1="12.5" y1="12.5" x2="20" y2="20" stroke="#fff" stroke-width="3"/></svg>
</header>

<svg class="abs arrow prev" viewBox="0 0 36 36"><circle cx="18" cy="18" r="16" fill="none" stroke="#9bcb3b" stroke-width="2.5"/><path d="M21 10 L12 18 L21 26 Z" fill="#9bcb3b"/></svg>
<svg class="abs arrow next" viewBox="0 0 36 36"><circle cx="18" cy="18" r="16" fill="none" stroke="#9bcb3b" stroke-width="2.5"/><path d="M15 10 L24 18 L15 26 Z" fill="#9bcb3b"/></svg>

<div class="abs hero-panel">
  <h1 class="hero-title">Leader of Yoga Teacher Training</h1>
  <p class="hero-text">Are you at a decision point in your life, where wellness has become a priority and you are seeking additional support to reach your goals?</p>
  <span class="btn-outline">Learn More</span>
</div>

<h2 class="abs section-title" style="top:798px">WELCOME TO <b>TOM PELLING</b></h2>
<p class="abs section-text" style="top:864px;left:255px;width:690px">Are you at a decision point in your life, where wellness has become a priority and you are seeking additional support to reach your goals? Crossroads Path Wellness offers a unique, exciting innovation in wellness and nutrition: health coaching. As a Certified Health Coach, I…</p>
<div class="abs read-more" style="top:952px">READ MORE &gt;&gt;</div>
<div class="abs rule" style="top:1024px"></div>

<h2 class="abs section-title" style="top:1068px">IMAGE <b>GALLERY</b></h2>
<p class="abs section-text" style="top:1120px">Lorem Ipsum is simply dummy text of the printing and typesetting industry. Lorem Ipsum has been the industry's standard dummy text ever since the 1500s, scracimen book.</p>

<div class="abs tile" style="left:98px;top:1202px;width:321px;height:230px;background:linear-gradient(135deg,#c9352a,#e0b23a 45%,#6b8a2e 70%,#3a3f7a)" role="img" aria-label="Colourful fresh fruit and vegetables"></div>
<div class="abs tile" style="left:440px;top:1202px;width:321px;height:230px;background:linear-gradient(180deg,#7ea25a,#9a8a7c 50%,#6a5a52)" role="img" aria-label="Group of yoga students posing outdoors"></div>
<div class="abs tile" style="left:98px;top:1452px;width:321px;height:231px;background:linear-gradient(180deg,#3f86bd,#2c6fa6 60%,#1f5c8c)" role="img" aria-label="Man practising yoga in the sea"></div>
<div class="abs tile" style="left:440px;top:1452px;width:321px;height:231px;background:linear-gradient(160deg,#b6a27a,#3f6a2f 45%,#6c7e4a)" role="img" aria-label="Assisted aerial yoga pose in a garden"></div>
<div class="abs tile overlay" style="left:781px;top:1202px;width:321px;height:481px;background:linear-gradient(180deg,#a4cf55,#95c440)" role="img" aria-label="Instructor guiding a student in a yoga pose">
  <svg width="42" height="42" viewBox="0 0 42 42"><circle cx="21" cy="21" r="19" fill="none" stroke="#fff" stroke-width="2.5"/><path d="M21 11v20M11 21h20" stroke="#fff" stroke-width="3.5"/></svg>
  <div class="overlay-label">Benefits At Any Age</div>
</div>

<div class="abs rule" style="top:1748px"></div>

<h2 class="abs section-title" style="top:1795px">OUR <b>TESTIMONIALS</b></h2>
<p class="abs section-text" style="top:1852px">Lorem Ipsum is simply dummy text of the printing and typesetting industry. Lorem Ipsum has been the industry's standard dummy text ever since the 1500s, scracimen book.</p>

<div class="abs tile" style="left:98px;top:1935px;width:337px;height:188px;background:linear-gradient(135deg,#6c6a6e,#9e8f8a 50%,#4e5f72)" role="img" aria-label="Video of a partner yoga class">
  <svg class="play" width="52" height="52" viewBox="0 0 52 52"><circle cx="26" cy="26" r="24" fill="none" stroke="#fff" stroke-width="2.5"/><path d="M21 16 L36 26 L21 36 Z" fill="#fff"/></svg>
</div>
<div class="abs tile" style="left:98px;top:2144px;width:337px;height:192px;background:linear-gradient(90deg,#c89a3c,#e6dccb 35%,#ece6dc 70%,#b9874a)" role="img" aria-label="Video of a triangle pose demonstration">
  <svg class="play" width="52" height="52" viewBox="0 0 52 52"><circle cx="26" cy="26" r="24" fill="none" stroke="#fff" stroke-width="2.5"/><path d="M21 16 L36 26 L21 36 Z" fill="#fff"/></svg>
</div>
<div class="abs tile" style="left:453px;top:1935px;width:649px;height:401px;background:linear-gradient(180deg,#c9c2b4,#8d8a80 50%,#5a5450)" role="img" aria-label="Video of a yoga class seated on mats in a studio">
  <svg class="play" width="64" height="64" viewBox="0 0 52 52"><circle cx="26" cy="26" r="24" fill="none" stroke="#fff" stroke-width="2.5"/><path d="M21 16 L36 26 L21 36 Z" fill="#fff"/></svg>
</div>

<section class="abs subscribe"></section>
<div class="abs sub-brand">Tom Pelling</div>
<div class="abs sub-title">SUBSCRIBE</div>
<div class="abs sub-script">Newsletter !</div>
<div class="abs field">ENTER EMAIL ADDRESS...</div>
<div class="abs sub-btn">SUBSCRIBE</div>

<footer>
  <div class="abs copyright">© 2015 All rights reserved.</div>
  <div class="abs social">
    <span style="background:#3b5998"></span>
    <span style="background:#2aa3dd"></span>
    <span style="background:#1f6fa8"></span>
    <span style="background:#d34836"></span>
    <span style="background:#c9252c"></span>
  </div>
</footer>

</body>
</html>
```